nukh almasira
nukh almasira - Corporate Services
Creative Brief
Simple
Kadhim Rubaie كاظم الربيعي
CEO المدير المفوض
Locality 482 - Alley 17 - House 8 Al Mansour - Baghdad - Iraq محلة 482 - زقاق 17 - دار 8 المنصور - بغداد - العراق
CEO@nukhalmasira.example
www.nukhalmasira.example
Concepts
Business Cards and Stationery for new compliance company.
Business Cards and Stationery for Background Check Company
qorvel42 qorvel42
good design but i hope you use the same name and information in the brief and if you can work on the logo cause i want to add the Arabic name of the company ( نخبة المسيرة ) if you can put the logo in the left and the name of the company in English and Arabic in the right of the logo and use the same font and size in Arabic and English name
Brisk Brisk
Ok
Please show me the whole stationary not only the business card
please use this e-mail on the letterhead only info@nukhalmasira.example and the address in arabic language use it only in the letterhead too thankyou

```html
<!DOCTYPE html>
<html lang="en">
<head>
<meta charset="utf-8">
<title>nukh almasira – business card</title>
<link href="https://fonts.googleapis.com/css2?family=Cinzel:wght@600&family=Open+Sans:wght@400;600;700&display=swap" rel="stylesheet">
<style>
  :root {
    --page: #e9eaec;
    --card: #ffffff;
    --blue: #2b8fd6;
    --blue-deep: #1f76b9;
    --orange: #f2a81d;
    --ink: #3d4650;
    --muted: #7b838c;
  }
  * { box-sizing: border-box; margin: 0; padding: 0; }
  html, body { width: 1200px; height: 901px; overflow: hidden; }
  body {
    background: var(--page);
    font-family: "Open Sans", Arial, sans-serif;
    color: var(--ink);
    display: flex;
    flex-direction: column;
    align-items: center;
    justify-content: center;
    gap: 60px;
  }
  .card {
    position: relative;
    width: 600px;
    height: 343px;
    background: var(--card);
    box-shadow: 0 10px 28px rgba(0,0,0,.14);
    overflow: hidden;
  }
  .card-art { position: absolute; inset: 0; width: 100%; height: 100%; }

  /* front */
  .brand {
    position: absolute;
    left: 150px; top: 112px;
    display: flex; align-items: center; gap: 16px;
  }
  .brand-mark {
    width: 54px; height: 54px; border-radius: 50%;
    background: var(--orange);
  }
  .brand-name {
    font-family: "Cinzel", Georgia, serif;
    font-weight: 600;
    font-size: 30px;
    letter-spacing: 1px;
    color: var(--blue-deep);
    text-transform: uppercase;
  }
  .front-address {
    position: absolute;
    left: 34px; bottom: 24px;
    color: #fff;
    font-size: 13px;
    line-height: 1.5;
    font-weight: 600;
  }

  /* back */
  .holder { position: absolute; left: 40px; top: 48px; }
  .holder-name {
    font-size: 22px; font-weight: 700; letter-spacing: 1px;
    color: var(--blue-deep); text-transform: uppercase;
  }
  .holder-role { font-size: 14px; color: var(--muted); margin-top: 2px; }
  .contacts {
    position: absolute; left: 40px; top: 150px;
    list-style: none; font-size: 14px; line-height: 2;
  }
  .contacts li { display: flex; align-items: center; gap: 10px; }
  .contacts svg { width: 14px; height: 14px; fill: var(--blue); }
</style>
</head>
<body>

  <section class="card card-front">
    <svg class="card-art" viewBox="0 0 600 343" aria-hidden="true">
      <path d="M0 250 C180 270 380 240 600 170 L600 190 C390 262 180 290 0 272 Z" fill="var(--orange)"/>
      <path d="M0 268 C190 290 400 258 600 186 L600 343 L0 343 Z" fill="var(--blue)"/>
    </svg>
    <div class="brand">
      <span class="brand-mark"></span>
      <span class="brand-name">Nukh Almasira</span>
    </div>
    <p class="front-address">Locality 482 - Alley 17<br>House 8 Al Mansour</p>
  </section>

  <section class="card card-back">
    <svg class="card-art" viewBox="0 0 600 343" aria-hidden="true">
      <path d="M500 0 L600 0 L600 18 C580 15 540 8 500 0 Z" fill="var(--orange)"/>
      <path d="M600 80 C520 170 480 260 470 343 L490 343 C500 270 540 180 600 104 Z" fill="var(--orange)"/>
      <path d="M600 104 C540 180 500 270 490 343 L600 343 Z" fill="var(--blue)"/>
    </svg>
    <div class="holder">
      <h1 class="holder-name">Kadhim Rubaie</h1>
      <p class="holder-role">Managing Director</p>
    </div>
    <ul class="contacts">
      <li><svg viewBox="0 0 24 24"><path d="M6.6 10.8a15 15 0 0 0 6.6 6.6l2.2-2.2a1 1 0 0 1 1-.25 11.4 11.4 0 0 0 3.6.57 1 1 0 0 1 1 1V20a1 1 0 0 1-1 1A17 17 0 0 1 3 4a1 1 0 0 1 1-1h3.5a1 1 0 0 1 1 1c0 1.25.2 2.45.57 3.57a1 1 0 0 1-.25 1Z"/></svg>011 555 0142</li>
      <li><svg viewBox="0 0 24 24"><path d="M6.6 10.8a15 15 0 0 0 6.6 6.6l2.2-2.2a1 1 0 0 1 1-.25 11.4 11.4 0 0 0 3.6.57 1 1 0 0 1 1 1V20a1 1 0 0 1-1 1A17 17 0 0 1 3 4a1 1 0 0 1 1-1h3.5a1 1 0 0 1 1 1c0 1.25.2 2.45.57 3.57a1 1 0 0 1-.25 1Z"/></svg>011 555 0187</li>
      <li><svg viewBox="0 0 24 24"><path d="M2 5h20v14H2Zm2 2v.5l8 5 8-5V7Zm0 2.8V17h16V9.8l-8 5Z"/></svg>CEO@nukhalmasira.example</li>
      <li><svg viewBox="0 0 24 24"><path d="M12 2a10 10 0 1 0 0 20 10 10 0 0 0 0-20Zm0 2c.9 1.2 1.6 2.6 2 4h-4c.4-1.4 1.1-2.8 2-4ZM4.3 14a8 8 0 0 1 0-4h3.4a16 16 0 0 0 0 4Zm.8 2h3a15 15 0 0 0 1.4 3.6A8 8 0 0 1 5.1 16Zm3-8h-3a8 8 0 0 1 4.4-3.6A15 15 0 0 0 8.1 8ZM12 20c-.9-1.2-1.6-2.6-2-4h4c-.4 1.4-1.1 2.8-2 4Zm2.3-6H9.7a14 14 0 0 1 0-4h4.6a14 14 0 0 1 0 4Zm.2 5.6A15 15 0 0 0 15.9 16h3a8 8 0 0 1-4.4 3.6ZM16.3 14a16 16 0 0 0 0-4h3.4a8 8 0 0 1 0 4Zm-.4-6a15 15 0 0 0-1.4-3.6A8 8 0 0 1 18.9 8Z"/></svg>www.nukhalmasira.example</li>
    </ul>
  </section>

</body>
</html>
```